Crust Harbor Hotel Coupon

Would like to design a coupon that is for hotels' staff and to be dropped off at the hotel front office anytime someone calls from a hotel and as a Thank You for hotel staff for recommending us. Coupon value to be $ 2.00. Should say Thank You or Thank you for recommending us. Need our phone number 250 614 3750 on it. Color scheme to be Green and Red as in the attached logo. Coupon to be designed for printing size 3.5 inches high and 7.5 inches wide. Rear should say Fastest Delivery, Favourite Pizza for Sports teams etc. Ask for group deals. Attached logo to be on the coupon. Coupon should say coupon # and space left for us write number

```html
<!DOCTYPE html>
<html lang="en">
<head>
<meta charset="utf-8">
<title>Crust Harbor Hotel Coupon</title>
<link rel="stylesheet" href="https://fonts.googleapis.com/css2?family=Arimo:wght@400;700&display=swap">
<style>
  :root {
    --paper: #f1f2f1;
    --mint-glow: #c9e6d2;
    --red-bright: #a3191b;
    --red-deep: #5a1414;
    --red-dark: #140d0d;
    --ink: #111111;
    --white: #ffffff;
    --brand-red: #b81d1f;
  }
  html, body {
    margin: 0;
    padding: 0;
    width: 1200px;
    height: 560px;
    overflow: hidden;
  }
  .coupon {
    position: relative;
    width: 1200px;
    height: 560px;
    overflow: hidden;
    font-family: "Arimo", Arial, sans-serif;
    background:
      radial-gradient(circle at 597px 284px, var(--mint-glow) 0, var(--mint-glow) 320px, rgba(201,230,210,0.55) 370px, rgba(241,242,241,0) 480px),
      var(--paper);
  }
  .value-disc {
    position: absolute;
    left: 272px;
    top: -41px;
    width: 650px;
    height: 650px;
    border-radius: 50%;
    background: linear-gradient(45deg, var(--red-dark) 12%, var(--red-deep) 50%, var(--red-bright) 90%);
    display: flex;
    align-items: center;
    justify-content: center;
  }
  .value-disc__label {
    color: var(--white);
    font-size: 31px;
    font-weight: 700;
    letter-spacing: 0.2px;
  }
  .thank-you {
    position: absolute;
    left: 915px;
    top: 84px;
    margin: 0;
    font-size: 25px;
    font-weight: 700;
    color: var(--ink);
  }
  .perks {
    position: absolute;
    left: 940px;
    top: 130px;
    width: 220px;
    margin: 0;
    font-size: 17px;
    line-height: 1.35;
    color: var(--ink);
  }
  .coupon-number {
    position: absolute;
    left: -100px;
    top: 273px;
    width: 400px;
    height: 30px;
    transform: rotate(-90deg);
    display: flex;
    align-items: flex-end;
    gap: 4px;
  }
  .coupon-number__label {
    font-size: 22px;
    font-weight: 700;
    color: var(--ink);
    line-height: 1;
  }
  .coupon-number__field {
    flex: 1;
    border-bottom: 2px solid var(--ink);
    margin-bottom: 2px;
  }
  .brand {
    position: absolute;
    left: 946px;
    top: 396px;
  }
  .brand__mark {
    display: flex;
    align-items: center;
    gap: 8px;
  }
  .brand__dot {
    width: 18px;
    height: 18px;
    border-radius: 50%;
    background: var(--brand-red);
  }
  .brand__name {
    font-size: 28px;
    font-weight: 700;
    color: var(--brand-red);
  }
  .brand__phone {
    margin: 8px 0 0 26px;
    font-size: 20px;
    font-weight: 700;
    color: var(--ink);
  }
</style>
</head>
<body>
  <main class="coupon">
    <div class="value-disc">
      <span class="value-disc__label">$2 Coupon</span>
    </div>
    <p class="thank-you">A big thank you!</p>
    <p class="perks">Fastest delivery. Favourite pizza for sports teams. Ask for group deals!</p>
    <div class="coupon-number">
      <span class="coupon-number__label">Coupon:</span>
      <span class="coupon-number__field"></span>
    </div>
    <div class="brand">
      <div class="brand__mark">
        <span class="brand__dot"></span>
        <span class="brand__name">Crust Harbor</span>
      </div>
      <p class="brand__phone">250 614 3750</p>
    </div>
  </main>
</body>
</html>
```